Etiketten für Deodorant in fester Form
Zielgruppe
Naturkosmetik
Aufgabenstellung
Dimension of the tube:
The height of the tube’s body is 53mm
The height of the lid is 20mm
The circular of the body is 126mm

```html
<!DOCTYPE html>
<html lang="de">
<head>
<meta charset="utf-8">
<title>Clairine – Zitrus Deo-Etikett</title>
<link rel="stylesheet" href="https://fonts.googleapis.com/css2?family=Cinzel:wght@400;600&family=Inter:wght@400&display=swap">
<style>
  :root {
    --stage: #1e1e1e;
    --label: #f7f7f7;
    --teal: #2fbfb8;
    --ink: #1a1a1a;
    --splash-blue: #d6e8f1;
    --splash-warm: #f3dcc0;
    --splash-green: #dbe9cf;
    --splash-rose: #efd3d6;
  }
  * { margin: 0; padding: 0; box-sizing: border-box; }
  html, body { width: 1200px; height: 857px; overflow: hidden; background: var(--stage); }
  .stage {
    width: 1200px; height: 857px;
    display: flex; flex-direction: column; align-items: center; justify-content: center;
    gap: 12px;
  }
  .lid-label, .body-label {
    width: 380px; background: var(--label); position: relative;
  }
  .lid-label {
    height: 240px;
    border-top: 10px solid var(--teal);
    border-bottom: 5px solid var(--teal);
    display: flex; align-items: center; justify-content: center;
  }
  .brand {
    display: flex; align-items: center; justify-content: center;
    width: 200px; height: 200px; border-radius: 50%;
    border: 2px solid var(--teal);
  }
  .brand-name {
    font-family: "Cinzel", serif; font-weight: 400;
    font-size: 30px; color: var(--teal); letter-spacing: 1px;
  }
  .body-label {
    height: 480px;
    border-top: 5px solid var(--teal);
    display: flex; flex-direction: column; align-items: center;
  }
  .product-name {
    margin-top: 48px;
    font-family: "Cinzel", serif; font-weight: 400;
    font-size: 78px; color: var(--teal); letter-spacing: 1px; line-height: 1;
  }
  .product-claims {
    margin-top: 18px;
    font-family: "Cinzel", serif; font-weight: 600;
    font-size: 18px; color: var(--ink); text-align: center; line-height: 1.3;
  }
  .net-weight {
    margin-top: 32px;
    font-family: "Inter", sans-serif; font-size: 24px; color: var(--teal); letter-spacing: 1px;
  }
  .fruit-splash {
    position: absolute; left: 0; right: 0; bottom: 20px; height: 200px;
    background:
      linear-gradient(180deg, var(--label) 0%, transparent 30%, transparent 80%, var(--label) 100%),
      linear-gradient(90deg, var(--splash-rose) 0%, var(--splash-warm) 30%, var(--splash-blue) 55%, var(--splash-green) 75%, var(--splash-warm) 100%);
  }
</style>
</head>
<body>
  <main class="stage">
    <section class="lid-label">
      <div class="brand"><span class="brand-name">Clairine</span></div>
    </section>
    <section class="body-label">
      <h1 class="product-name">ZITRUS</h1>
      <p class="product-claims">Naturkosmetik und BIO<br>Mit Cacao-butter</p>
      <p class="net-weight">50 G</p>
      <div class="fruit-splash" role="img" aria-label="Illustration: Wasserspritzer mit Orange, Limette, Kiwi, Granatapfel, Himbeeren und Blättern"></div>
    </section>
  </main>
</body>
</html>
```